Retail Photo Calendar of Anchorage, Alaska

I am a professional photographer in Anchorage, Alaska. I'm looking for a designer to create a unique, pleasing design for a 12-month (24 pages plus front and back cover) 2016 RETAIL calendar using images of mine of the Anchorage, Alaska area. This is not a promotional calendar. This calendar will be sold to the public in retail stores. So it's more about the calendar & photos than my name. Design must be appealing to the average consumer. The designer would be responsible for completing the entire calendar project to give plate-ready files. We’ll need both the raw InDesign files with links, as well as a PDF to be printed as a proof and submitted to the printer.

Specs for the calendar are:
• one vertical photo on front cover
• back cover
• inside back cover pages x 2
• Grid page for each month
• 12 horizontal photos for the monthly pages based on these specifications:
o Size: 8 7/8” x 12”
o Pages: Front and Back Cover plus 24 pages

Attached are two sample designs, one I like (file name “sample inside good”) and one I don’t like (sample inside bad). The one I like and what I’d want for my calendar is;
• more elegant design than the bad design
• small photo inserted on the grid page
• Unique fonts
• Nice ghosted back design element (sun in this case—which matches the month of July in Alaska)
• A quote

The one I don’t like (bad) is:
• Too much like a block
• Fonts are not very elegant
• Not much in the way of design going on here

I will supply:
• Excell document with approximately 100 dates for holiday’s, moon phases and special days.
• High resolution files of the 13 main images and 12 smaller insets
• Copy for each month including; captions for photos, quotes etc.
• The actual dates for a 2016 calendar

In order for me to choose a designer, what I’m expecting for this initial design is for the designer to offer the following;

1. A design for the cover, using the vertical image of the dog team supplied - and this copy: Anchorage, Alaska & Vicinity 2016 Calendar Photography by Dale Brannock

2. A design for ONE month on the inside--- ( 2 pages) photo placement, caption, calendar grid, design element, quote, small photo and previous/next month small grid. Do this using the one horizontal photo (airplanes) supplied – and greeking text for the potential copy of the photo caption, quote, etc.

A sample of what I'm looking for the designer to send me to choose their design is in the file labeled: "Cover and Inside Sample" --- the picture of an existing cover & inside of a calendar.

Once I choose the design and designer I prefer, he/she and I will then work together as I supply the rest of the images, dates and copy as mentioned above. Tweaks to be made as we go along. The deadline for the print-ready final, is to be completed by August 15, 2014 -- Once the final complete designs are made and confirmed to work for the printer is when I'll pay the designer the amount pledged.

PLEASE feel free to contact me before starting design work if I can help clarify what I am looking for here.

Target Market(s)

The general public living in or visiting Anchorage, Alaska

Industry/Entity Type

Printer

Font styles to use
Serif

Requirements
Must have
• elegant pleasing design

```html
<!DOCTYPE html>
<html lang="en">
<head>
<meta charset="utf-8">
<title>Anchorage, Alaska &amp; Vicinity 2016 Calendar – April</title>
<link rel="stylesheet" href="https://fonts.googleapis.com/css2?family=Cinzel:wght@400;600&family=Cormorant+Garamond:ital,wght@0,400;0,600;1,400&display=swap">
<style>
  :root{
    --gold:#c49a3a;
    --gold-dark:#a87f27;
    --gold-soft:#f3ead6;
    --gold-ghost:rgba(196,154,58,.08);
    --ink:#6b5a3a;
    --line:#d9d4c8;
    --cell:#ffffff;
    --empty:#f4f2ee;
    --paper:#ffffff;
  }
  *{box-sizing:border-box;margin:0;padding:0}
  html,body{width:882px;height:1200px;overflow:hidden;background:var(--paper)}
  .page{position:relative;width:882px;height:1200px;overflow:hidden;background:var(--paper);font-family:"Cormorant Garamond",Georgia,serif;color:var(--ink)}
  .ghost-sun{position:absolute;left:430px;top:560px;width:520px;height:520px;pointer-events:none}
  .hero-photo{position:absolute;left:11px;top:16px;width:860px;height:496px;
    background:linear-gradient(180deg,#bcd6ea 0%,#d7e7f2 26%,#eef2f4 36%,#6f9fc6 46%,#8db6d6 60%,#e9eef2 74%,#f7f9fa 100%)}
  .quote{position:absolute;left:11px;top:522px;width:300px;font-size:13px;line-height:1.35;color:var(--gold-dark);font-style:italic}
  .quote cite{display:block;font-style:normal;font-family:"Cinzel",serif;font-size:10px;letter-spacing:1px;margin-top:2px}
  .contact{position:absolute;left:441px;top:536px;list-style:none;font-size:12.5px;line-height:1.2;color:var(--ink)}
  .contact li{display:flex;align-items:center;gap:6px;margin-bottom:2px}
  .contact svg{width:11px;height:11px;flex:none}
  .photographer{position:absolute;right:11px;top:552px;font-family:"Cinzel",serif;font-weight:400;font-size:22px;letter-spacing:1px;color:var(--gold)}
  .sidebar{position:absolute;left:11px;top:622px;width:154px}
  .mini-month{text-align:center}
  .mini-month h3{font-family:"Cinzel",serif;font-weight:400;font-size:12px;letter-spacing:1px;color:var(--gold-dark);margin-bottom:2px}
  .mini-grid{display:grid;grid-template-columns:repeat(7,1fr);font-size:10.5px;line-height:14px;color:var(--ink)}
  .mini-grid .dow{color:var(--gold-dark);font-weight:600}
  .side-caption{margin-top:10px;font-size:11.5px;line-height:1.3;font-style:italic;color:var(--gold-dark)}
  .inset-photo{margin-top:6px;width:154px;height:79px;background:linear-gradient(180deg,#bcd4e6 0%,#e9eff3 40%,#b57a45 60%,#eef2f4 80%,#f8fafb 100%)}
  .title-block{margin-top:6px;height:168px;background:var(--gold);color:#fff;text-align:center;padding-top:22px}
  .title-block .place{font-family:"Cinzel",serif;font-size:14px;letter-spacing:1.5px;line-height:1.3}
  .title-block .year{font-family:"Cinzel",serif;font-size:34px;font-weight:600;margin-top:4px}
  .title-block .name{font-family:"Cinzel",serif;font-size:13px;letter-spacing:1px;margin-top:8px}
  .next-month{margin-top:16px}
  .month-name{position:absolute;right:11px;top:610px;font-family:"Cinzel",serif;font-weight:400;font-size:56px;letter-spacing:3px;color:var(--gold)}
  .calendar{position:absolute;left:176px;top:704px;width:695px}
  .weekdays{display:grid;grid-template-columns:repeat(7,1fr);height:32px;align-items:center;text-align:center;font-family:"Cinzel",serif;font-size:13px;letter-spacing:.5px;color:var(--gold)}
  .days{display:grid;grid-template-columns:repeat(7,1fr);grid-auto-rows:89.6px;border-top:1px solid var(--line);border-left:1px solid var(--line)}
  .day{border-right:1px solid var(--line);border-bottom:1px solid var(--line);background:rgba(255,255,255,.82);position:relative}
  .day.weekend{background:rgba(243,234,214,.85)}
  .day.empty{background:rgba(244,242,238,.85)}
  .day span{position:absolute;left:0;top:0;width:28px;height:28px;background:var(--gold);color:#fff;font-family:"Cinzel",serif;font-size:15px;line-height:28px;text-align:center}
</style>
</head>
<body>
<main class="page">
  <svg class="ghost-sun" viewBox="0 0 520 520" aria-hidden="true">
    <circle cx="260" cy="260" r="250" fill="var(--gold-ghost)"/>
    <circle cx="260" cy="260" r="180" fill="none" stroke="var(--gold-ghost)" stroke-width="14"/>
  </svg>

  <div class="hero-photo" role="img" aria-label="Photo: two red foxes sparring on snowy shore beside blue water, frosted shrub and snow-capped mountains behind"></div>
  <blockquote class="quote">“In the quiet of early spring, the wild things of the north remember how to play.”<cite>— Alaskan saying</cite></blockquote>
  <ul class="contact">
    <li><svg viewBox="0 0 12 12"><circle cx="6" cy="6" r="5.5" fill="var(--gold)"/></svg>Brannock Images</li>
    <li><svg viewBox="0 0 12 12"><path d="M3 1.5h2l1 2.5-1.3 1a6 6 0 0 0 2.3 2.3l1-1.3 2.5 1v2a1 1 0 0 1-1 1A8.5 8.5 0 0 1 2 2.5a1 1 0 0 1 1-1z" fill="var(--gold)"/></svg>907-555-0142</li>
    <li><svg viewBox="0 0 12 12"><rect x="1" y="2.5" width="10" height="7" fill="none" stroke="var(--gold)"/><path d="M1 2.5l5 4 5-4" fill="none" stroke="var(--gold)"/></svg>info@brannockimages.com</li>
    <li><svg viewBox="0 0 12 12"><path d="M6 1a3.5 3.5 0 0 0-3.5 3.5C2.5 7.5 6 11 6 11s3.5-3.5 3.5-6.5A3.5 3.5 0 0 0 6 1z" fill="var(--gold)"/><circle cx="6" cy="4.5" r="1.2" fill="#fff"/></svg>www.brannockimages.com</li>
  </ul>
  <div class="photographer">Dale Brannock</div>

  <aside class="sidebar">
    <section class="mini-month">
      <h3>MARCH</h3>
      <div class="mini-grid">
        <span class="dow">S</span><span class="dow">M</span><span class="dow">T</span><span class="dow">W</span><span class="dow">T</span><span class="dow">F</span><span class="dow">S</span>
        <span></span><span></span><span>1</span><span>2</span><span>3</span><span>4</span><span>5</span>
        <span>6</span><span>7</span><span>8</span><span>9</span><span>10</span><span>11</span><span>12</span>
        <span>13</span><span>14</span><span>15</span><span>16</span><span>17</span><span>18</span><span>19</span>
        <span>20</span><span>21</span><span>22</span><span>23</span><span>24</span><span>25</span><span>26</span>
        <span>27</span><span>28</span><span>29</span><span>30</span><span>31</span><span></span><span></span>
      </div>
    </section>
    <p class="side-caption">Two young foxes greet the first warm days of the season near Anchorage.</p>
    <div class="inset-photo" role="img" aria-label="Small photo: foxes on snow by the water"></div>
    <div class="title-block">
      <div class="place">ANCHORAGE<br>ALASKA<br>&amp; VICINITY</div>
      <div class="year">2016</div>
      <div class="name">Dale Brannock</div>
    </div>
    <section class="mini-month next-month">
      <h3>MAY</h3>
      <div class="mini-grid">
        <span class="dow">S</span><span class="dow">M</span><span class="dow">T</span><span class="dow">W</span><span class="dow">T</span><span class="dow">F</span><span class="dow">S</span>
        <span>1</span><span>2</span><span>3</span><span>4</span><span>5</span><span>6</span><span>7</span>
        <span>8</span><span>9</span><span>10</span><span>11</span><span>12</span><span>13</span><span>14</span>
        <span>15</span><span>16</span><span>17</span><span>18</span><span>19</span><span>20</span><span>21</span>
        <span>22</span><span>23</span><span>24</span><span>25</span><span>26</span><span>27</span><span>28</span>
        <span>29</span><span>30</span><span>31</span><span></span><span></span><span></span><span></span>
      </div>
    </section>
  </aside>

  <h1 class="month-name">APRIL</h1>
  <section class="calendar">
    <div class="weekdays"><span>Sunday</span><span>Monday</span><span>Tuesday</span><span>Wednesday</span><span>Thursday</span><span>Friday</span><span>Saturday</span></div>
    <div class="days">
      <div class="day empty"></div><div class="day empty"></div><div class="day empty"></div><div class="day empty"></div><div class="day empty"></div><div class="day"><span>1</span></div><div class="day weekend"><span>2</span></div>
      <div class="day weekend"><span>3</span></div><div class="day"><span>4</span></div><div class="day"><span>5</span></div><div class="day"><span>6</span></div><div class="day"><span>7</span></div><div class="day"><span>8</span></div><div class="day weekend"><span>9</span></div>
      <div class="day weekend"><span>10</span></div><div class="day"><span>11</span></div><div class="day"><span>12</span></div><div class="day"><span>13</span></div><div class="day"><span>14</span></div><div class="day"><span>15</span></div><div class="day weekend"><span>16</span></div>
      <div class="day weekend"><span>17</span></div><div class="day"><span>18</span></div><div class="day"><span>19</span></div><div class="day"><span>20</span></div><div class="day"><span>21</span></div><div class="day"><span>22</span></div><div class="day weekend"><span>23</span></div>
      <div class="day weekend"><span>24</span></div><div class="day"><span>25</span></div><div class="day"><span>26</span></div><div class="day"><span>27</span></div><div class="day"><span>28</span></div><div class="day"><span>29</span></div><div class="day weekend"><span>30</span></div>
    </div>
  </section>
</main>
</body>
</html>
```